4th Generation Family Business Needs a New Card Design!

We are a family owned 4th Generation company. We are based in the Sydney, Australia area and we are desperately in need of a more modern and classy card. We are monumental masons who design, supply & erect lasting memorials throughout cemeteries in Sydney. Our customers are normally in a period of grieving. I have attached logo files that will need to be implemented on the card. Company was established 1935. Australian Owned and Operated. Card needs to be designed to PRINTLY.com specification.

Target Market(s)

Our target market is based upon people that a grieving for family members that have passed away. We also deal with alot of companies that own and operate cemeteries.

Industry/Entity Type

Business

Contact Information for Business Card

Oliver Brantley, Operations Manager, 0417552908, oliver@hollowaystoneworks.com.au
Martin Brantley, Director, 0431906627, martin@hollowaystoneworks.com.au
Phone # 02 9634 2258
Website: www.hollowaystoneworks.com.au
Address: Suite 17, 8 Calloway Lane, East Penrose, Sydney NSW 2290

Font styles to use
Serif
Decorative
Script

Requirements
Must have
• Would like to see the logo nicely implemented with a modern design. Embossed lettering would be a nice additive.

```html
<!DOCTYPE html>
<html lang="en">
<head>
<meta charset="utf-8">
<title>Holloway Stoneworks – Business Card</title>
<link href="https://fonts.googleapis.com/css2?family=Cinzel:wght@600;700&family=Playfair+Display:wght@400;700&display=swap" rel="stylesheet">
<style>
  :root {
    --bg: #e9e6e1;
    --card-white: #fbfbfa;
    --card-black: #0d0d0d;
    --ink: #141414;
    --gold: #d9be2c;
    --gold-band: #d6bc2a;
    --rule-gold: #e4d27a;
    --white: #f4f4f2;
  }
  * { box-sizing: border-box; margin: 0; padding: 0; }
  html, body { width: 1200px; height: 780px; overflow: hidden; }
  body {
    background: var(--bg);
    position: relative;
    font-family: "Playfair Display", Georgia, serif;
    color: var(--ink);
  }
  .card {
    position: absolute;
    border-radius: 16px;
    overflow: hidden;
    box-shadow: 0 10px 28px rgba(0,0,0,.18);
  }

  /* Front */
  .card-front {
    left: 150px; top: 110px;
    width: 340px; height: 560px;
    background: var(--card-white);
    text-align: center;
  }
  .front-brand { padding-top: 58px; }
  .brand-name {
    font-family: "Cinzel", serif;
    font-weight: 700;
    color: var(--ink);
    line-height: 1.05;
    letter-spacing: 2px;
  }
  .front-brand .brand-name .line-1 { display: block; font-size: 34px; }
  .front-brand .brand-name .line-2 { display: block; font-size: 20px; letter-spacing: 5px; margin-top: 4px; }
  .brand-rule {
    width: 260px; height: 1px; margin: 16px auto 0;
    background: var(--gold);
  }
  .person { margin-top: 22px; }
  .person-name {
    font-family: "Cinzel", serif;
    font-weight: 700;
    font-size: 19px;
    letter-spacing: 2px;
  }
  .person-title {
    font-size: 15px;
    color: var(--gold);
    margin-top: 2px;
  }
  .contact { margin-top: 14px; }
  .contact-item {
    padding: 7px 0 6px;
    border-top: 1px solid var(--rule-gold);
    width: 250px; margin: 0 auto;
  }
  .contact-item:first-child { border-top: none; }
  .contact-label {
    display: block;
    font-size: 10px;
    font-weight: 700;
    color: var(--gold);
    letter-spacing: .5px;
  }
  .contact-value { display: block; font-size: 14px; font-weight: 700; }
  .contact-value.email { font-size: 12.5px; }
  .address {
    margin-top: 12px;
    font-size: 13.5px;
    font-weight: 700;
    line-height: 1.35;
  }
  .front-band {
    position: absolute; left: 0; right: 0; bottom: 0;
    height: 66px;
    background: var(--gold-band);
    border-top: 3px solid var(--ink);
    display: flex; align-items: center; justify-content: center;
    font-size: 14px; font-weight: 700;
  }

  /* Back */
  .card-back {
    left: 560px; top: 250px;
    width: 520px; height: 330px;
    background: var(--card-black);
    display: flex; flex-direction: column; align-items: center; justify-content: center;
  }
  .card-back .brand-name {
    color: var(--white);
    text-align: center;
  }
  .card-back .brand-name .line-1 { display: block; font-size: 60px; letter-spacing: 4px; }
  .card-back .brand-name .line-2 { display: block; font-size: 30px; letter-spacing: 9px; margin-top: 6px; }
  .back-rule { width: 360px; height: 2px; background: var(--gold); margin: 20px 0 16px; }
  .back-web { font-size: 14px; font-weight: 700; color: var(--gold); letter-spacing: .5px; }
</style>
</head>
<body>

  <section class="card card-front">
    <div class="front-brand">
      <div class="brand-name"><span class="line-1">HOLLOWAY</span><span class="line-2">STONEWORKS</span></div>
      <div class="brand-rule"></div>
    </div>

    <div class="person">
      <div class="person-name">OLIVER BRANTLEY</div>
      <div class="person-title">Operations Manager</div>
    </div>

    <div class="contact">
      <div class="contact-item">
        <span class="contact-label">Mobile</span>
        <span class="contact-value">0417552908</span>
      </div>
      <div class="contact-item">
        <span class="contact-label">Phone</span>
        <span class="contact-value">02 9634 2258</span>
      </div>
      <div class="contact-item">
        <span class="contact-label">Email</span>
        <span class="contact-value email">oliver@hollowaystoneworks.com.au</span>
      </div>
    </div>

    <p class="address">Suite 17, 8 Calloway Lane,<br>East Penrose, Sydney NSW 2290</p>

    <div class="front-band">www.hollowaystoneworks.com.au</div>
  </section>

  <section class="card card-back">
    <div class="brand-name"><span class="line-1">HOLLOWAY</span><span class="line-2">STONEWORKS</span></div>
    <div class="back-rule"></div>
    <div class="back-web">www.hollowaystoneworks.com.au</div>
  </section>

</body>
</html>
```